Kveldbrá - Start-up company selling electricity

Hello let me tell you about Kveldbrá.

Kveldbrá is start-up company selling electricity in Iceland. The operations of the company consist of making power usage forecasts for our customers, purchasing the electricity wholesale from the energy producers, and selling the electricity to the consumer. We are focused on tech by using optimization and machine learning to minimize electricity prices to our customers. Our marketing strategy is to portray a tech company mindset and to show dedication to driving down the electricity price on the market.

We need your help to make our website pop. Possible concepts to work with are as follows:

- Iceland the land of ice and fire
- Green energy
- Innovation
- Tech and data science

Link to our website: https://prufa.kveldbra.is/
We are open to ideas.
Thank you!

Target Market(s)

Electricity consumers both homes and companies.

Number of Pages Required

1 page

Font styles to use
Serif
Sans Serif

```html
<!DOCTYPE html>
<html lang="en">
<head>
<meta charset="utf-8">
<title>Kveldbrá – Same electricity, just cheaper</title>
<link href="https://fonts.googleapis.com/css2?family=Cinzel:wght@400;600;700&family=Poppins:wght@300;400;500;600&display=swap" rel="stylesheet">
<style>
:root{
  --navy:#1b3461;
  --navy-soft:#44597f;
  --red:#a9322a;
  --red-soft:#b9544a;
  --ink:#222;
  --muted:#555;
  --white:#fff;
  --serif:'Cinzel', serif;
  --sans:'Poppins', sans-serif;
}
*{margin:0;padding:0;box-sizing:border-box}
html,body{width:1200px;height:2826px;overflow:hidden;background:var(--white)}
body{position:relative;font-family:var(--sans);color:var(--ink)}
.abs{position:absolute}
.btn{position:absolute;display:flex;align-items:center;justify-content:center;border-radius:26px;text-decoration:none}
.btn-red{background:var(--red);color:var(--white)}
.btn-navy{background:var(--navy);color:var(--white)}

/* header */
.site-header{position:absolute;left:0;top:0;width:1200px;height:84px;background:var(--white)}
.brand{position:absolute;left:82px;top:24px;display:flex;align-items:center;gap:10px;font-family:var(--serif);font-weight:700;font-size:28px;color:var(--red)}
.brand-dot{width:26px;height:26px;border-radius:50%;background:var(--navy)}
.nav a{position:absolute;top:36px;font-family:var(--serif);font-size:15px;color:var(--navy);text-decoration:none}
.nav a.active{color:var(--red);text-decoration:underline}

/* hero */
.hero-art{left:0;top:84px}
.hero-title{left:0;width:1200px;text-align:center;font-family:var(--serif);font-weight:700;color:var(--white)}
.hero-cta{left:463px;top:518px;width:274px;height:52px;font-family:var(--serif);font-weight:700;font-size:20px}

/* welcome */
.welcome-title{left:612px;top:792px;font-family:var(--serif);font-size:31px;color:var(--navy);font-weight:600}
.welcome-name{left:612px;top:830px;font-family:var(--serif);font-size:44px;color:var(--red);font-weight:700}
.welcome-text{left:612px;top:893px;width:460px;font-size:13.5px;line-height:25.6px;color:#333}
.read-more{left:616px;top:1049px;width:157px;height:45px;font-weight:600;font-size:15px}

.tagline{left:0;width:1200px;text-align:center;font-family:var(--serif);font-weight:700;color:#111}

/* split band */
.band{left:0;top:1367px}
.band-heading{font-family:var(--serif);font-size:30px;color:var(--white);font-weight:600}
.band-btn{top:1620px;width:180px;height:44px;font-family:var(--serif);font-size:22px;font-weight:600}
.price{font-size:40px;font-weight:600;color:var(--white);text-align:center;width:170px;line-height:1}
.price-unit{font-size:15px;color:var(--white);text-align:center;width:170px;line-height:20px}
.price-cta{left:760px;top:1655px;width:257px;height:46px;background:var(--white);color:var(--navy);font-family:var(--serif);font-size:22px;font-weight:600}

/* testimonials */
.t-title{left:0;top:1840px;width:1200px;text-align:center;font-family:var(--serif);font-size:36px;font-weight:700;color:var(--navy)}
.t-sub{left:0;top:1887px;width:1200px;text-align:center;font-size:15px;color:var(--muted)}
.t-photo{left:196px;top:1981px;width:360px;height:224px;border-radius:140px 6px 6px 140px;background:linear-gradient(135deg,#e6e2de,#b7a79b 55%,#3d4e66)}
.t-avatar{left:511px;top:2050px;width:84px;height:84px;border-radius:50%;border:5px solid var(--white);background:linear-gradient(160deg,#d9d4cf,#3b3633)}
.t-quote{left:635px;top:1985px;width:370px;font-size:13.5px;line-height:19.2px;color:#333}
.t-client{left:635px;top:2120px;font-size:17px;color:var(--red)}
.dots span{position:absolute;top:2178px;width:9px;height:9px;border-radius:50%;background:#ddd}

/* footer */
.footer-art{left:0;top:2260px}
.c-title{left:0;top:2390px;width:1200px;text-align:center;font-family:var(--serif);font-size:37px;font-weight:700;color:var(--white)}
.field{position:absolute;background:var(--white);font-size:14px;color:#444;padding:9px 14px;height:32px}
.submit{left:591px;top:2675px;width:109px;height:33px;font-weight:600;font-size:14px}
.info-title{left:789px;top:2472px;font-size:21px;font-weight:600;color:var(--white)}
.info-icon{position:absolute;left:778px;width:37px;height:37px;border-radius:50%;background:#d9423a}
.info-text{position:absolute;left:828px;font-size:15px;line-height:19px;color:var(--white);width:220px}
.social{position:absolute;top:2677px;width:33px;height:33px;border-radius:50%;border:1.5px solid var(--white)}
.rule{left:158px;top:2750px;width:868px;height:1px;background:rgba(255,255,255,.35)}
.copy{left:0;top:2774px;width:1200px;text-align:center;font-size:14px;color:var(--white)}
</style>
</head>
<body>

<header class="site-header">
  <div class="brand"><span class="brand-dot"></span>KVELDBRÁ</div>
  <nav class="nav">
    <a class="active" href="#" style="left:487px">HOME</a>
    <a href="#" style="left:580px">TERMS OF BUSINESS</a>
    <a href="#" style="left:770px">ASKED &amp; ANSWERED</a>
    <a href="#" style="left:947px">ABOUT KVELDBRÁ</a>
  </nav>
</header>

<svg class="abs hero-art" width="1200" height="620" viewBox="0 84 1200 620">
  <defs>
    <radialGradient id="heroGlow" cx="50%" cy="45%" r="70%">
      <stop offset="0" stop-color="#5a3ea8"/>
      <stop offset=".45" stop-color="#221a4a"/>
      <stop offset="1" stop-color="#060816"/>
    </radialGradient>
    <linearGradient id="heroFloor" x1="0" x2="1">
      <stop offset="0" stop-color="#3a2a70"/>
      <stop offset=".35" stop-color="#c04fc8"/>
      <stop offset=".7" stop-color="#4b8fc4"/>
      <stop offset="1" stop-color="#1d2a55"/>
    </linearGradient>
  </defs>
  <g role="img" aria-label="Glowing light bulb standing on a cracked surface under a network of light points">
    <rect x="0" y="84" width="1200" height="620" fill="url(#heroGlow)"/>
    <rect x="0" y="470" width="1200" height="234" fill="url(#heroFloor)" opacity=".55"/>
  </g>
  <path d="M0 575 Q600 780 1200 575 L1200 704 L0 704 Z" fill="var(--white)"/>
  <path d="M165 617 Q600 735 1050 617" fill="none" stroke="var(--red)" stroke-width="4"/>
  <circle cx="600" cy="670" r="24" fill="var(--red)"/>
  <path d="M594 658 L606 670 L594 682" fill="none" stroke="var(--white)" stroke-width="2.5"/>
</svg>
<div class="abs hero-title" style="top:372px;font-size:46px">SAME ELECTRICITY</div>
<div class="abs hero-title" style="top:428px;font-size:58px">JUST CHEEPER!</div>
<a class="btn btn-red hero-cta" href="#">PRICE COMPARISON</a>

<!-- welcome -->
<svg class="abs" style="left:110px;top:740px" width="450" height="420" viewBox="110 740 450 420">
  <circle cx="334" cy="950" r="200" fill="none" stroke="var(--navy)" stroke-width="8"/>
  <circle cx="334" cy="950" r="182" fill="#1a1a1a" role="img" aria-label="Rows of clear light bulbs with one glowing amber bulb"/>
  <circle cx="334" cy="950" r="182" fill="url(#none)" opacity="0"/>
  <circle cx="138" cy="955" r="22" fill="var(--navy)" stroke="var(--white)" stroke-width="4"/>
  <circle cx="527" cy="955" r="22" fill="var(--navy)" stroke="var(--white)" stroke-width="4"/>
</svg>
<div class="abs welcome-title">WELCOME TO</div>
<div class="abs welcome-name">KVELDBRÁ</div>
<p class="abs welcome-text">Lorem Ipsum is simply dummy text of the printing and typesetting industry. Lorem Ipsum has been the industry's standard dummy text ever since the 1500s, when an unknown printer took a galley of type and scrambled it to make. Lorem Ipsum is simply dummy text of the printing and typesetting industry. Lorem Ipsum has been the industry's standard dummy.</p>
<a class="btn btn-red read-more" href="#">READ MORE</a>

<div class="abs tagline" style="top:1234px;font-size:36px">SAME ELECTRICITY</div>
<div class="abs tagline" style="top:1276px;font-size:48px">JUST CHEAPER!</div>

<!-- split band -->
<svg class="abs band" width="1200" height="396" viewBox="0 1367 1200 396">
  <rect x="0" y="1367" width="1200" height="396" fill="var(--navy-soft)" role="img" aria-label="Power lines over a misty landscape in blue tones"/>
  <path d="M562 1367 L1200 1367 L1200 1763 L666 1763 Z" fill="var(--red-soft)" role="img" aria-label="Hand holding a light bulb in red tones"/>
  <path d="M562 1367 L666 1763" stroke="var(--white)" stroke-width="5"/>
  <circle cx="610" cy="1565" r="42" fill="var(--white)"/>
  <circle cx="610" cy="1570" r="18" fill="var(--navy)"/>
  <circle cx="332" cy="1490" r="34" fill="none" stroke="var(--white)" stroke-width="3"/>
  <circle cx="790" cy="1465" r="28" fill="none" stroke="var(--white)" stroke-width="3"/>
  <line x1="877" y1="1533" x2="877" y2="1620" stroke="var(--white)" stroke-width="1.5"/>
</svg>
<div class="abs band-heading" style="left:0;width:664px;text-align:center;top:1548px">REGISTER NOW</div>
<a class="btn btn-red band-btn" href="#" style="left:154px">COMPANY</a>
<a class="btn btn-navy band-btn" href="#" style="left:346px">HOME</a>
<div class="abs band-heading" style="left:833px;top:1452px">OUR PRICE</div>
<div class="abs price" style="left:710px;top:1537px">6.95</div>
<div class="abs price-unit" style="left:710px;top:1578px">Kronur/kWst</div>
<div class="abs price" style="left:891px;top:1537px">6.95</div>
<div class="abs price-unit" style="left:891px;top:1578px">Kronur/kWst<br>rafmagnskynding</div>
<a class="btn price-cta" href="#">PRICE COMPARISON</a>

<!-- testimonials -->
<div class="abs t-title">CLIENT TESTIMONIALS</div>
<div class="abs t-sub">Lorem Ipsum is simply dummy text of the printing</div>
<svg class="abs" style="left:500px;top:1915px" width="200" height="45">
  <line x1="2" y1="22" x2="80" y2="22" stroke="var(--navy)" stroke-width="1.5"/>
  <line x1="120" y1="22" x2="198" y2="22" stroke="var(--navy)" stroke-width="1.5"/>
  <circle cx="100" cy="24" r="12" fill="var(--navy)"/>
</svg>
<div class="abs t-photo" role="img" aria-label="Smiling couple sitting together on a sofa"></div>
<div class="abs t-avatar" role="img" aria-label="Portrait of the client"></div>
<p class="abs t-quote">Lorem Ipsum is simply dummy text of the printing and typesetting industry. Lorem Ipsum has been the indus-try's standard dummy text ever since the 1500s, when an unknown printer took a galley of type and scrambled it to make a type specimen book. It has survived not only five centuries,</p>
<div class="abs t-client">Client Name</div>
<div class="dots"><span style="left:637px;background:var(--red)"></span><span style="left:654px"></span><span style="left:671px"></span><span style="left:688px"></span></div>
<svg class="abs" style="left:920px;top:2172px" width="70" height="20">
  <path d="M24 10 H4 M11 3 L4 10 L11 17" fill="none" stroke="#777" stroke-width="1.6"/>
  <path d="M44 10 H64 M57 3 L64 10 L57 17" fill="none" stroke="#777" stroke-width="1.6"/>
</svg>

<!-- footer -->
<svg class="abs footer-art" width="1200" height="566" viewBox="0 2260 1200 566">
  <path d="M0 2390 Q600 2250 1200 2390 L1200 2826 L0 2826 Z" fill="var(--navy)"/>
  <path d="M150 2368 Q600 2270 1040 2368" fill="none" stroke="var(--red)" stroke-width="6"/>
  <circle cx="600" cy="2315" r="40" fill="var(--white)"/>
  <circle cx="600" cy="2322" r="18" fill="var(--navy)"/>
</svg>
<div class="abs c-title">CONTACT US</div>
<div class="field" style="left:158px;top:2481px;width:267px">Name</div>
<div class="field" style="left:433px;top:2481px;width:267px">Phone</div>
<div class="field" style="left:158px;top:2522px;width:542px">Email</div>
<div class="field" style="left:158px;top:2563px;width:542px;height:90px">Message</div>
<a class="btn btn-red submit" href="#">SUBMIT</a>

<div class="abs info-title">CONTACT US</div>
<span class="info-icon" style="top:2540px"></span>
<svg class="abs" style="left:778px;top:2540px" width="37" height="160">
  <path d="M18.5 9 a6 6 0 0 1 6 6 c0 5 -6 11 -6 11 s-6 -6 -6 -11 a6 6 0 0 1 6 -6z" fill="var(--white)"/>
  <circle cx="18.5" cy="15" r="2.2" fill="#d9423a"/>
</svg>
<span class="info-icon" style="top:2594px"></span>
<svg class="abs" style="left:778px;top:2594px" width="37" height="37">
  <path d="M12 10 l4 0 l2 5 l-2.5 2 a11 11 0 0 0 5 5 l2 -2.5 l5 2 l0 4 a2 2 0 0 1 -2 2 a17 17 0 0 1 -15.5 -15.5 a2 2 0 0 1 2 -2z" fill="var(--white)"/>
</svg>
<span class="info-icon" style="top:2642px"></span>
<svg class="abs" style="left:778px;top:2642px" width="37" height="37">
  <rect x="10" y="12" width="17" height="13" rx="1.5" fill="var(--white)"/>
  <path d="M10 13 L18.5 20 L27 13" fill="none" stroke="#d9423a" stroke-width="1.5"/>
</svg>
<div class="info-text" style="top:2531px">233, Lorem Ipsum is simply dummy text of the</div>
<div class="info-text" style="top:2603px">(888) 888 8888</div>
<div class="info-text" style="top:2651px">info@kveldbra.is</div>
<span class="social" style="left:784px"></span>
<span class="social" style="left:823px"></span>
<span class="social" style="left:862px"></span>
<span class="social" style="left:902px"></span>

<div class="abs rule"></div>
<div class="abs copy">© 2021 Kveldbrá. All Rights are Reserved.</div>

</body>
</html>
```